The Lantern Below

I have a faux cover I will attach & want you to follow & enhance what I've created. Just an FYI, the book will be posted on pebblor & I'm working with Tallow Quill Printhouse.
What you need to know:
The dimensions: 6" x 9" (15.24 x 22.86 cm)
Background color: Black
I did not capture the color of the font, so want you to get a similar gold color.
Font for title, subtitle & author name: Goudy Old Style
Font for "20th Anniversary Edition": Kunstler Script
I have thoughts of shaping the photo in an oval shape -- possibly shade out the edges?

Target Market(s)

All ages: anyone who has encountered issues with doctors, hospitals, and especially those who have struggled with cancer treatment.

Requirements
Nice to have
• Adding below another PDF, showing vintage lines that I would like to see used. Just added some text I will add to the back cover. I am waiting on one more review, which I will add. Attaching that below.

```html
<!DOCTYPE html>
<html lang="en">
<head>
<meta charset="UTF-8">
<title>The Lantern Below — 20th Anniversary Edition Cover</title>
<link rel="stylesheet" href="https://fonts.googleapis.com/css2?family=Sorts+Mill+Goudy:ital@0;1&display=swap">
<style>
  :root {
    --page: #ffffff;
    --cover-black: #0b0b0b;
    --gold-light: #fbf1d2;
    --gold-mid: #e4c88a;
    --gold-deep: #a8813f;
    --gold-flare: #e9a43a;
    --ink-dark: #1a1a1a;
    --grey-mid: #8c8c8c;
    --grey-light: #e6e6e6;
  }
  * { margin: 0; padding: 0; box-sizing: border-box; }
  html, body {
    width: 1200px; height: 800px; overflow: hidden;
    background: var(--page);
  }
  .canvas {
    position: relative; width: 1200px; height: 800px;
    display: flex; align-items: center; justify-content: center;
  }
  .cover {
    position: relative; width: 480px; height: 720px; overflow: hidden;
    background: var(--cover-black);
    font-family: "Sorts Mill Goudy", "Goudy Old Style", serif;
  }
  .cover-glow {
    position: absolute; inset: 0;
    background:
      radial-gradient(ellipse 75% 45% at 55% 50%, var(--grey-light) 0%, var(--grey-mid) 45%, rgba(0,0,0,0) 80%),
      linear-gradient(160deg, #1c1c1c 0%, #5a5a5a 25%, #9a9a9a 40%, #1c1c1c 88%);
  }
  .portrait {
    position: absolute; left: 40px; top: 230px; width: 420px; height: 380px;
    border-radius: 50%;
    background: radial-gradient(ellipse at 55% 50%, #d4d4d4 0%, #9d9d9d 45%, rgba(60,60,60,0) 72%);
  }
  .sparkle {
    position: absolute; right: -30px; top: -20px; width: 190px; height: 150px;
    background: radial-gradient(ellipse at 70% 40%, rgba(233,164,58,0.7) 0%, rgba(168,110,40,0.3) 40%, rgba(0,0,0,0) 72%);
  }
  .gold-text {
    background: linear-gradient(180deg, var(--gold-light) 0%, var(--gold-mid) 55%, var(--gold-deep) 100%);
    -webkit-background-clip: text; background-clip: text; color: transparent;
  }
  .title {
    position: absolute; left: 0; right: 0; top: 44px;
    text-align: center; line-height: 0.95; letter-spacing: 1px; font-weight: 400;
  }
  .title-line { display: block; }
  .title-small { font-size: 34px; }
  .title-large { font-size: 70px; }
  .title-line--second { padding-left: 70px; }
  .subtitle {
    position: absolute; left: 40px; right: 20px; top: 192px;
    text-align: center; font-size: 16.5px; line-height: 1.3; color: var(--ink-dark);
  }
  .flare {
    position: absolute; left: 0; bottom: 0; width: 320px; height: 170px;
  }
  .edition-mark {
    position: absolute; left: 56px; top: 556px; width: 100px; height: 100px;
  }
  .edition {
    position: absolute; left: 168px; top: 568px;
    font-style: italic; line-height: 1.05;
  }
  .edition-main { display: block; font-size: 34px; }
  .edition-sub { display: block; font-size: 28px; padding-left: 44px; }
  .author {
    position: absolute; right: 22px; top: 658px; font-size: 26px; letter-spacing: 0.5px;
  }
</style>
</head>
<body>
<main class="canvas">
  <article class="cover">
    <div class="cover-glow"></div>
    <div class="portrait" role="img" aria-label="Black and white portrait of the author, oval with softly faded edges"></div>
    <div class="sparkle" role="img" aria-label="Scattered gold bokeh sparkles"></div>

    <h1 class="title gold-text">
      <span class="title-line"><span class="title-small">THE</span> <span class="title-large">LANTERN</span></span>
      <span class="title-line title-line--second"><span class="title-large">BELOW</span></span>
    </h1>

    <p class="subtitle">A tale of lifelong damage from terminal<br>cancer “treatment” &amp; inhumane doctors</p>

    <svg class="flare" viewBox="0 0 320 170" role="img" aria-label="Flowing gold light swoosh">
      <defs>
        <linearGradient id="flareGold" x1="0" y1="0" x2="1" y2="0">
          <stop offset="0" stop-color="#e9a43a" stop-opacity="0.9"/>
          <stop offset="0.6" stop-color="#f4d68f" stop-opacity="0.7"/>
          <stop offset="1" stop-color="#000000" stop-opacity="0"/>
        </linearGradient>
      </defs>
      <path d="M0 80 C60 60 120 130 200 130 C250 130 290 120 320 110 L320 170 L0 170 Z" fill="url(#flareGold)"/>
    </svg>

    <svg class="edition-mark" viewBox="0 0 100 100" aria-hidden="true">
      <circle cx="50" cy="50" r="47" fill="#0b0b0b" stroke="#e4c88a" stroke-width="3"/>
    </svg>

    <p class="edition gold-text">
      <span class="edition-main">20th Anniversary</span>
      <span class="edition-sub">Edition</span>
    </p>

    <p class="author gold-text">Mara Ellison</p>
  </article>
</main>
</body>
</html>
```